Präsentationsvorlagen für Verkaufsgespräche
Zielgruppe
Wir verkaufen hochwertigen Kaffee, der traditionel im Trommelröster langsam geröstet wird. Unsere Zielgruppe sind W/ M 30-70.
Aufgabenstellung
Mit dieser Vorlage möchte ich bei den ersten Verkaufsgesprächen unsere Firma gut repräsentieren. Das wird keine lange Präsentation, soll aber einen ansprechenden Einstieg ins Gespräch sein.
Ein paar Fotos habe ich beigefügt. Texte füge ich später ein, wenn jemand was griffbereit hat, nehme ich aber auch das gerne.

```html
<!DOCTYPE html>
<html lang="de">
<head>
<meta charset="utf-8">
<title>Molinero Kaffee – Präsentationsvorlage</title>
<link rel="stylesheet" href="https://fonts.googleapis.com/css2?family=Open+Sans:wght@300;400;600;700&family=Roboto:wght@300;400;500&display=swap">
<style>
  :root {
    --page: #ededed;
    --ink: #2b2a29;
    --paper: #ffffff;
    --panel: #f2f2f2;
    --text: #333333;
    --label: #222222;
  }
  * { margin: 0; padding: 0; box-sizing: border-box; }
  html, body { width: 783px; height: 1200px; overflow: hidden; background: var(--page); }
  body { position: relative; font-family: "Roboto", Arial, sans-serif; color: var(--text); }

  .slide-label { position: absolute; width: 120px; margin-left: -60px; text-align: center;
    font: 600 11px "Open Sans", Arial, sans-serif; color: var(--label); }
  .slide-label.faint { color: rgba(255,255,255,.75); }

  .slide { position: absolute; background: var(--paper); overflow: hidden;
    box-shadow: 0 4px 10px rgba(0,0,0,.18); }
  .slide-lg { left: 73px; top: 64px; width: 638px; height: 478px; }
  .slide-sm { width: 298px; height: 223px; }

  .dark { position: absolute; background: var(--ink); }
  .photo { position: absolute; }
  .abs { position: absolute; }

  .heading { font-weight: 500; color: #2b2a29; text-transform: uppercase; line-height: 1.1; }
  .body-copy { font-size: 6.1px; line-height: 9px; color: #333; font-weight: 400; }
  .body-copy p + p { margin-top: 2px; }

  /* slide 1 */
  .brand { position: absolute; left: 0; width: 319px; text-align: center; color: #fff; }
  .brand-mark { position: absolute; left: 130px; top: 160px; width: 58px; height: 58px;
    border: 2px solid #fff; border-radius: 50%; }
  .brand-name { top: 226px; font: 700 26px "Open Sans", Arial, sans-serif; }
  .brand-title { top: 284px; font: 700 16px "Open Sans", Arial, sans-serif; }
  .brand-url { top: 309px; font: 400 12px "Open Sans", Arial, sans-serif; letter-spacing: 2.6px; }
  .story-box { position: absolute; left: 424px; top: 83px; width: 214px; height: 312px;
    background: var(--panel); padding: 26px 28px 0 32px; }
  .story-box .heading { font-size: 15px; }
  .story-lead { margin: 14px 0 14px; font-size: 9px; line-height: 11.5px; font-weight: 300; color: #2b2a29; }

  .slide-title { font-size: 12px; font-weight: 500; color: #2b2a29; }
  .bullets { list-style: none; font-size: 8.5px; line-height: 10px; color: #2b2a29; }
  .bullets li { padding-left: 8px; text-indent: -8px; margin-bottom: 5px; }
  .bullets li::before { content: "•"; display: inline-block; width: 8px; text-indent: 0; }
  .tile { position: absolute; width: 86px; height: 86px; background: var(--panel); }
  .tile .photo { left: 8px; top: 6px; width: 70px; height: 74px; }

  .hex { position: absolute; }
  .hex-text { position: absolute; text-align: center; font-weight: 500; color: #2b2a29; line-height: 1.2; }
  .hex-text.sm { font-size: 11.5px; }
  .hex-text.md { font-size: 12px; }

  .footer-band { position: absolute; left: 0; top: 1123px; width: 783px; height: 77px; background: var(--ink); }
  .footer-title { position: absolute; left: 0; top: 1138px; width: 783px; text-align: center;
    font: 300 37px "Open Sans", Arial, sans-serif; color: #fff; letter-spacing: 1px; }
</style>
</head>
<body>

<div class="slide-label" style="left:388px; top:38px;">SLIDE 1</div>
<section class="slide slide-lg">
  <div class="dark" style="left:0; top:0; width:319px; height:478px;"></div>
  <div class="photo" role="img" aria-label="Espresso fließt aus dem Siebträger in eine weiße Tasse"
       style="left:159px; top:31px; width:479px; height:416px; background: radial-gradient(ellipse at 35% 55%, #e6e2dc 0%, #cfc7bc 35%, #8a7660 65%, #3a2e25 100%);"></div>
  <div class="brand-mark"></div>
  <div class="brand brand-name">Molinero</div>
  <div class="brand brand-title">Molinero Kaffee</div>
  <div class="brand brand-url">www.molinero-kaffee.de</div>
  <div class="story-box">
    <h1 class="heading">Unsere<br>Kaffeegeschichte</h1>
    <p class="story-lead">Wir verkaufen hochwertigen Kaffee, der traditionel im Trommelröster langsam geröstet wird.</p>
    <div class="body-copy">
      <p>Lorem ipsum dolor sit amet, consectetur adipiscing elit, sed do eiusmod tempor incididunt ut labore et dolore magna aliqua. Nisi porta lorem mollis aliquam ut porttitor leo a diam. Non arcu risus quis varius quam quisque. Feugiat in fermentum posuere urna nec tincidunt praesent semper feugiat. Diam quam nulla porttitor massa id neque aliqu</p>
      <p>am vestibulum morbi. Sed odio morbi quis commodo odio. Varius quam quisque id diam vel quam elementum pulvinar etiam. Ut pharetra sit amet aliquam id diam maecenas ultricies mi. Mi sit amet mauris commodo quis imperdiet massa tincidunt nunc. Justo nec ultrices dui sapien eget mi proin sed libero. Pellentesque sit amet porttitor eget dolor morbi non arcu. Pretium quam vulputate dignissim suspendisse. Molestie a iaculis at erat pellentesque adipiscing. Egestas maecenas pharetra convallis posuere morbi leo.Diam quam nulla porttitor massa id neque</p>
    </div>
  </div>
</section>

<div class="slide-label" style="left:223px; top:554px;">SLIDE 2</div>
<section class="slide slide-sm" style="left:73px; top:579px;">
  <div class="dark" style="left:149px; top:0; width:149px; height:223px;"></div>
  <h2 class="slide-title abs" style="left:17px; top:9px;">Unsere Kaffeemarken</h2>
  <ul class="bullets abs" style="left:17px; top:36px;">
    <li>Crema Dorada</li>
    <li>Expresso<br>Finca Alta</li>
  </ul>
  <div class="body-copy abs" style="left:17px; top:77px; width:75px;">
    <p>Lorem ipsum dolor sit amet, consectetur adipiscing elit, sed do eiusmod tempor incididunt ut labore et dolore magna aliqua. Nisi porta lorem mollis aliquam ut porttitor leo a diam. Non arcu risus quis varius quam quisque. Feugiat in fermentum posuere urna nec tincidunt praesent semper feugiat. Diam quam nulla porttitor</p>
  </div>
  <div class="tile" style="left:102px; top:28px;">
    <div class="photo" role="img" aria-label="Goldene Kaffeepackung mit orangefarbenem Sortenetikett" style="background: linear-gradient(90deg, #c9a24a 0%, #e8d49a 40%, #d2562a 70%, #f2f2f2 100%);"></div>
  </div>
  <div class="tile" style="left:192px; top:28px;">
    <div class="photo" role="img" aria-label="Drei helle Kaffeepackungen nebeneinander" style="background: linear-gradient(180deg, #efe4cf 0%, #dcc39f 55%, #c08a63 80%, #e6d3b4 100%);"></div>
  </div>
  <div class="tile" style="left:102px; top:118px;">
    <div class="photo" role="img" aria-label="Drei silberschwarze Kaffeepackungen nebeneinander" style="background: linear-gradient(180deg, #3a3a3c 0%, #8c8c90 45%, #d9a48a 65%, #2f2f31 100%);"></div>
  </div>
  <div class="tile" style="left:192px; top:118px;">
    <div class="photo" role="img" aria-label="Schwarze Kaffeepackung mit weinrotem Sortenetikett" style="background: linear-gradient(90deg, #2a2a2a 0%, #6f6f6f 40%, #8f1d3b 70%, #f2f2f2 100%);"></div>
  </div>
</section>

<div class="slide-label" style="left:561px; top:554px;">SLIDE 3</div>
<section class="slide slide-sm" style="left:412px; top:579px;">
  <h2 class="slide-title heading abs" style="left:22px; top:21px;">Die Kaffeegeschichte</h2>
  <div class="body-copy abs" style="left:22px; top:43px; width:142px;">
    <p>Lorem ipsum dolor sit amet, consectetur adipiscing elit, sed do eiusmod tempor incididunt ut labore et dolore magna aliqua.</p>
    <p style="margin-top:4px;">Nisi porta lorem mollis aliquam ut porttitor leo a diam. Non arcu risus quis varius quam quisque.</p>
  </div>
  <div class="photo" role="img" aria-label="Geröstete Kaffeebohnen im Kühlsieb des Trommelrösters"
       style="left:0; top:112px; width:298px; height:111px; background: linear-gradient(160deg, #6b4a35 0%, #8a6247 35%, #5a3b28 65%, #3b2619 100%);"></div>
  <svg class="hex" style="left:193px; top:56px;" width="74" height="84" viewBox="0 0 74 84" aria-hidden="true">
    <polygon points="37,0 74,21 74,63 37,84 0,63 0,21" fill="#f4f4f4"/>
  </svg>
  <div class="hex-text md" style="left:193px; top:88px; width:74px;">ÜBER<br>KAFFEE</div>
</section>

<div class="slide-label" style="left:223px; top:810px;">SLIDE 4</div>
<section class="slide slide-sm" style="left:73px; top:835px;">
  <div class="dark" style="left:0; top:0; width:83px; height:223px;"></div>
  <div class="abs" style="left:17px; top:42px; width:189px; height:139px; background:#fff;"></div>
  <div class="photo" role="img" aria-label="Zwei Hände halten geröstete Kaffeebohnen"
       style="left:21px; top:46px; width:181px; height:131px; background: radial-gradient(ellipse at 55% 55%, #7a5a44 0%, #4d3526 35%, #1e1612 75%, #141110 100%);"></div>
  <h2 class="slide-title heading abs" style="right:13px; top:24px;">Über Kaffee</h2>
  <div class="body-copy abs" style="left:214px; top:48px; width:75px;">
    <p>Lorem ipsum dolor sit amet, consectetur adipiscing elit, sed do eiusmod tempor incididunt ut labore et dolore magna aliqua. Nisi porta lorem mollis aliquam ut porttitor leo a diam. Non arcu risus quis varius quam quisque. Feugiat in fermentum posuere urna nec tincidunt praesent semper feugiat. Diam quam nulla porttitor massa id neque aliqu</p>
    <p style="margin-top:4px;">am vestibulum morbi. Sed odio morbi quis commodo odio. Varius quam quisque</p>
  </div>
</section>

<div class="slide-label" style="left:561px; top:810px;">SLIDE 5</div>
<section class="slide slide-sm" style="left:412px; top:835px;">
  <div class="photo" role="img" aria-label="Nahaufnahme gerösteter Kaffeebohnen in einer Metallschaufel"
       style="left:0; top:0; width:217px; height:223px; background: radial-gradient(ellipse at 60% 45%, #8a6446 0%, #5b3d29 35%, #2e1d16 70%, #3a1414 100%);"></div>
  <svg class="hex" style="left:17px; top:13px;" width="50" height="58" viewBox="0 0 50 58" aria-hidden="true">
    <polygon points="25,0 50,14.5 50,43.5 25,58 0,43.5 0,14.5" fill="#fff"/>
  </svg>
  <div class="hex-text sm" style="left:17px; top:29px; width:50px;">ÜBER<br>KAFFEE</div>
  <div class="body-copy abs" style="left:224px; top:44px; width:68px;">
    <p>Lorem ipsum dolor sit amet, consectetur adipiscing elit, sed do eiusmod tempor incididunt ut labore et dolore magna aliqua.</p>
    <p style="margin-top:4px;">Nisi porta lorem mollis aliquam ut porttitor leo a diam. Non arcu risus quis varius quam quisque. Feugiat in fermentum posuere urna nec tincidunt praesent semper feugiat. Diam quam nulla porttitor massa id neque aliqu</p>
    <p style="margin-top:4px;">am vestibulum morbi. Sed odio morbi quis</p>
  </div>
</section>

<div class="slide-label faint" style="left:223px; top:1066px;">SLIDE 6</div>
<div class="slide-label faint" style="left:561px; top:1066px;">SLIDE 7</div>

<div class="footer-band"></div>
<div class="footer-title">POWERPOINT TEMPLATE</div>

</body>
</html>
```